Business Card for a Candle Company. - Creative Hipster Styling :)

I am after a two sided Business Card. Contact information on the front, text that will be supplied (and details further on here) on the back. Ideally I am looking for someone I can continue to work with in the future for flyers, labels, marketing material etc.

I have a Logo which I am using as the labels for the candle and have attached all the versions of the file I was given. I am after a similar feel to my logo and love the font and the feather used. it is important that my card looks like it is meant to go with the logo.

I would love you to use your imagination and see what can be thought up :)

All my candles are either clear or black glass and packaging is black and labels are white, on a square label with black writing (see attachments)

I love the feather on the logo if it can be incorporated great, if the business card looks better without it than that is fine too..

Target Market(s)

I am a new candle company and the feel I'm going for is a little luxury a little hipster. Imagine the candle going into a converted warehouse studio in the city.

Industry/Entity Type

Home And Garden

Contact Information for Business Card

I have a Logo which I am using as the labels for the candle and have attached all the versions of the file I was given. I am after a similar feel to my logo and love the font used but its caps and I don't really want everything in CAPS. It is important thought that everything goes together.

I love the feather on the logo if it can be incorporated great, if the business card looks better without it than that is fine too.

Morrel Wick Co
Saltmarsh Bay, QLD Australia
A little wax company, in a garage, on the coast.
craftlane.example/au/shop/MorrelWickCo
friendspace.example.au/morrelwickco
morrelwickco@mailbox.example.au
Jess Holloran
0481 572 316.

On the back of the card I need it to look good and go with the design on the front but want a bit of text;

To give you an idea of what I want on the back I've put what I've got following but I'm still working on grammar and wording so it may change slightly before the final edit.

We would love to see how you display your candle or reuse the glass vessel and would love to see a photo!
Check out ideas and share yours on your social media #morrelwickco

Just a few ideas to reuse your vessel;

A Vase to Display fresh flowers
Lolly Jar for your favourite candy
Decorate with baubles at Christmas
Bathroom Vanity Storage
Decorate with eggs at Easter
Plant a teranium inside.

Font styles to use
Decorative
Script
Other font styles liked:
• OctinVintageFree

Colors
000000
ffffff
757575

Requirements
Must have
• The only must is that it needs to look like it goes with my logo which I am using as the labels on the actual candle. the labels are white with black details and are square.
• Not too structured if possible as it is a creative company rather that a professional services company.
• I want people to pick up the card and think it looks great. I believe a business card is a very useful marketing tool and should be used as such. One card will be included in with each candle so that customers can re order.
Nice to have
• I love the feather on the logo if it can be incorporated great, if the business card looks better without it than that is fine too.
• Card just needs to fit with the logo.
Should not have
• It should not be a boring card. :)

```html
<!DOCTYPE html>
<html lang="en">
<head>
<meta charset="utf-8">
<title>Morrel Wick Co — Business Card</title>
<link href="https://fonts.googleapis.com/css2?family=Montserrat:wght@300;400;600&display=swap" rel="stylesheet">
<style>
  :root {
    --stage: #141414;
    --card: #2b2b2b;
    --ink: #ffffff;
    --muted: #d9d9d9;
    --shadow: rgba(0, 0, 0, 0.55);
  }
  * { margin: 0; padding: 0; box-sizing: border-box; }
  html, body {
    width: 1200px;
    height: 720px;
    overflow: hidden;
    background: var(--stage);
    font-family: "Montserrat", Arial, sans-serif;
    color: var(--ink);
  }
  .canvas {
    width: 1200px;
    height: 720px;
    display: flex;
    align-items: center;
    justify-content: center;
    gap: 40px;
  }
  .card {
    position: relative;
    width: 540px;
    height: 310px;
    background: var(--card);
    border-radius: 20px;
    box-shadow: 0 18px 40px var(--shadow);
  }

  /* Brand name in place of the logo lockup */
  .brand {
    display: flex;
    align-items: center;
    gap: 10px;
    font-weight: 400;
    font-size: 20px;
    letter-spacing: 0.18em;
    text-transform: uppercase;
    color: var(--ink);
    white-space: nowrap;
  }
  .brand-dot {
    width: 10px;
    height: 10px;
    border-radius: 50%;
    background: var(--ink);
    flex: none;
  }

  /* Front */
  .card-front .brand { position: absolute; left: 40px; top: 52px; }
  .holder-name {
    position: absolute;
    right: 44px;
    top: 48px;
    font-weight: 600;
    font-size: 19px;
    white-space: nowrap;
  }
  .contact-list {
    position: absolute;
    left: 40px;
    bottom: 38px;
    list-style: none;
    font-size: 14px;
    font-weight: 400;
    line-height: 1.55;
    color: var(--muted);
  }
  .contact-list li { display: flex; align-items: center; gap: 10px; white-space: nowrap; }
  .contact-icon { width: 12px; height: 12px; flex: none; }
  .contact-list .no-icon { padding-left: 22px; }

  /* Back */
  .card-back {
    display: flex;
    flex-direction: column;
    align-items: center;
    justify-content: center;
    gap: 46px;
  }
  .card-back .brand { font-size: 26px; }
  .tagline {
    font-weight: 300;
    font-size: 18px;
    letter-spacing: 0.02em;
    white-space: nowrap;
  }
</style>
</head>
<body>
  <main class="canvas">

    <section class="card card-front" aria-label="Card front">
      <div class="brand"><span class="brand-dot"></span>Morrel Wick Co</div>
      <div class="holder-name">Jess Holloran</div>
      <ul class="contact-list">
        <li>
          <svg class="contact-icon" viewBox="0 0 12 12" aria-hidden="true"><circle cx="6" cy="6" r="5" fill="#ffffff"/></svg>
          morrelwickco
        </li>
        <li>
          <svg class="contact-icon" viewBox="0 0 12 12" aria-hidden="true"><path d="M2.5 1h2l1 2.5-1.3 1a6 6 0 0 0 3.3 3.3l1-1.3L11 7.5v2A1.5 1.5 0 0 1 9.5 11 8.5 8.5 0 0 1 1 2.5 1.5 1.5 0 0 1 2.5 1z" fill="#ffffff"/></svg>
          0481 572 316
        </li>
        <li>
          <svg class="contact-icon" viewBox="0 0 12 12" aria-hidden="true"><rect x="0.5" y="2.5" width="11" height="7" fill="#ffffff"/><path d="M0.5 2.5 6 6.5l5.5-4" stroke="#2b2b2b" stroke-width="1" fill="none"/></svg>
          morrelwickco@mailbox.example.au
        </li>
        <li>
          <svg class="contact-icon" viewBox="0 0 12 12" aria-hidden="true"><circle cx="6" cy="6" r="5" fill="none" stroke="#ffffff" stroke-width="1.2"/><ellipse cx="6" cy="6" rx="2.2" ry="5" fill="none" stroke="#ffffff" stroke-width="1"/><path d="M1 6h10" stroke="#ffffff" stroke-width="1"/></svg>
          craftlane.example/au/shop/MorrelWickCo
        </li>
        <li class="no-icon">Saltmarsh Bay, QLD</li>
      </ul>
    </section>

    <section class="card card-back" aria-label="Card back">
      <div class="brand"><span class="brand-dot"></span>Morrel Wick Co</div>
      <p class="tagline">A candle maker, by the bay, in a small shed</p>
    </section>

  </main>
</body>
</html>
```